Help me create an email template that looks good

Hello, I need some help to create an email template that looks professional. I have some examples I can send to the right person. It should be a quick and easy job. Quick review and payment offered. I already have a logo and colour scheme. I will add files later today with exact requirements and preferences.
I need something that will just appear and look good on mobile device without having to worry about images being blocked or left out.

PLEASE DO NOT SUBMIT ENTIES UNTIL ADD SAMPLE, LOGO, COLOURS ETC

```html
<!DOCTYPE html>
<html lang="en">
<head>
<meta charset="utf-8">
<title>Lumiere – Welcome Email</title>
<link rel="stylesheet" href="https://fonts.googleapis.com/css2?family=Lato:wght@400;700&family=Parisienne&display=swap">
<style>
  :root {
    --page-bg: #e8e8e8;
    --panel-dark: #3a3a3a;
    --panel-light: #ffffff;
    --accent: #dd2f71;
    --accent-heading: #d23a72;
    --body-text: #3d3d3d;
    --fine-text: #333333;
    --icon-grey: #8c8c8c;
    --divider: #cfcfcf;
  }
  * { margin: 0; padding: 0; box-sizing: border-box; }
  html, body { width: 1200px; height: 2304px; overflow: hidden; }
  body {
    position: relative;
    background: var(--page-bg);
    font-family: "Lato", Arial, sans-serif;
    color: var(--body-text);
  }
  .preheader {
    position: absolute; top: 116px; left: 0; width: 1200px;
    text-align: center; font-size: 16.5px; color: var(--fine-text);
  }
  .preheader a { color: var(--fine-text); text-decoration: underline; }

  .email { position: absolute; left: 126px; top: 156px; width: 945px; }
  .email-header {
    height: 157px; background: var(--panel-dark);
    border-top: 3px solid var(--panel-light);
    display: flex; align-items: center; justify-content: center;
  }
  .brand-name {
    font-family: "Lato", Arial, sans-serif; font-weight: 400;
    color: var(--panel-light); font-size: 52px; letter-spacing: 1px;
  }
  .hero {
    position: relative; height: 531px;
    background: radial-gradient(ellipse at 55% 45%, #c9a58a 0%, #8f6a4f 45%, #b9b4ad 100%);
  }
  .hero-label {
    position: absolute; left: 0; right: 0; bottom: 24px;
    text-align: center; color: #ffffff; font-size: 27px; letter-spacing: 0.5px;
  }

  .email-body { background: var(--panel-light); height: 953px; position: relative; }
  .welcome-title {
    position: absolute; top: 38px; left: 0; right: 0; text-align: center;
    font-family: "Parisienne", cursive; font-size: 84px; color: var(--accent-heading);
    line-height: 1;
  }
  .intro {
    position: absolute; left: 52px; top: 146px; width: 830px;
    font-size: 25px; line-height: 32px;
  }
  .intro p + p { margin-top: 32px; }
  .cta {
    position: absolute; left: 342px; top: 432px; width: 250px; height: 73px;
    background: var(--accent); color: #ffffff; font-size: 27px;
    display: flex; align-items: center; justify-content: center; text-decoration: none;
  }
  .divider {
    position: absolute; left: 21px; top: 550px; width: 902px; height: 2px;
    background: var(--divider);
  }
  .services-title {
    position: absolute; top: 593px; left: 0; right: 0; text-align: center;
    font-size: 36px; color: var(--accent-heading); font-weight: 400;
  }
  .service { position: absolute; top: 662px; width: 240px; }
  .service-1 { left: 52px; } .service-2 { left: 351px; } .service-3 { left: 651px; }
  .service-image { height: 159px; }
  .service-image.sea { background: linear-gradient(180deg, #d98bb8 0%, #9a7fb0 50%, #4a4358 100%); }
  .service-image.city { background: linear-gradient(180deg, #4b8fd6 0%, #8fb6d8 55%, #5b6b63 100%); }
  .service-image.beach { background: linear-gradient(180deg, #6f86a8 0%, #c99a6e 60%, #e0cfa8 100%); }
  .service-caption { margin-top: 20px; font-size: 22.5px; line-height: 30px; }

  .email-footer {
    background: var(--panel-dark); height: 192px;
    display: flex; flex-direction: column; align-items: center;
  }
  .social { display: flex; gap: 23px; margin-top: 43px; }
  .social-icon { width: 54px; height: 54px; border-radius: 8px; background: var(--icon-grey); }
  .contact { margin-top: 33px; color: #ffffff; font-size: 20px; }
  .contact b { font-weight: 700; }
  .contact .sep { margin: 0 18px; }

  .legal {
    position: absolute; left: 0; top: 2016px; width: 1200px;
    text-align: center; font-size: 16.5px; line-height: 27px; color: var(--fine-text);
  }
  .legal p + p { margin-top: 27px; }
  .legal a { color: var(--fine-text); }
</style>
</head>
<body>
  <p class="preheader">Something not looking right? <a href="#">View the web version</a></p>

  <main class="email">
    <header class="email-header">
      <span class="brand-name">Lumiere</span>
    </header>

    <div class="hero" role="img" aria-label="Hero banner photo of a woman with long wavy hair in a warm-toned setting">
      <span class="hero-label">Hero banner 600X356px.</span>
    </div>

    <section class="email-body">
      <h1 class="welcome-title">Wecome to All</h1>
      <div class="intro">
        <p>Lorem ipsum dolor sit amet, consectetuer adipiscing elit. Nam nibh. Nunc varius facilisis eros. Sed erat. In in velit quis arcu ornare laoreet. Curabitur adipiscing luctus massa.</p>
        <p>Integer ut purus ac augue commodo commodo. Nunc nec mi eu justo tempor consectetuer. Etiam vitae nisl. In dignissim lacus ut ante. Cras elit lectus, bibendum a, adipiscing vitae, commodo et, dui.</p>
      </div>
      <a class="cta" href="#">View Offers</a>
      <div class="divider"></div>

      <h2 class="services-title">Our Services</h2>
      <div class="service service-1">
        <div class="service-image sea" role="img" aria-label="Photo of rocks in a calm sea under a pink sunset sky"></div>
        <p class="service-caption">Lorem ipsum dolor sit amet,</p>
      </div>
      <div class="service service-2">
        <div class="service-image city" role="img" aria-label="Photo of a harbour statue in front of a city skyline"></div>
        <p class="service-caption">Lorem ipsum dolor sit amet,</p>
      </div>
      <div class="service service-3">
        <div class="service-image beach" role="img" aria-label="Photo of beachfront high-rise towers at sunset"></div>
        <p class="service-caption">Lorem ipsum dolor sit amet,</p>
      </div>
    </section>

    <footer class="email-footer">
      <div class="social">
        <span class="social-icon" aria-label="Social link"></span>
        <span class="social-icon" aria-label="Social link"></span>
        <span class="social-icon" aria-label="Social link"></span>
      </div>
      <p class="contact">Email: <b>hello@lumierestudio.com</b><span class="sep">|</span>Web: <b>www.lumierestudio.com</b></p>
    </footer>
  </main>

  <div class="legal">
    <p>This email was sent to you because you requested it from www.lumierestudio.com<br>Please do not reply to this email.</p>
    <p><a href="#">Click here</a> to unsubscribe or manage your email preferences.</p>
    <p>Our mailing address: 45 Harbor Lane, Portland, USA. 54321</p>
    <p>© 2017 Lumiere Studio. All rights reserved.</p>
  </div>
</body>
</html>
```